KVT Business Cards

We require business cards for our business. We would like a matte black back to the card, with our logo centred in the middle. The front side of the card is open to design.

Target Market(s)

Clients looking for legal services (professional)

Industry/Entity Type

Legal

Contact Information for Business Card

Boris Telemark
Partner
Mobile: 0438 715 642
Email: boris@kvtlaw.co
Website: www.kvtlaw.co
Level 3, 118 Wexbury Street
Sydney NSW 2000

Font styles to use
Other font styles liked:
• Avenir

Colors
f04a50
ffffff
1b1b1b

Requirements
Must have
• Black back with logo included in the centre of the card.
• Our font is Avenir.

```html
<!DOCTYPE html>
<html lang="en">
<head>
<meta charset="utf-8">
<title>KVT Legal – Business Cards</title>
<link rel="stylesheet" href="https://fonts.googleapis.com/css2?family=Nunito+Sans:ital,wght@0,400;0,600;0,700;0,800&family=Playfair+Display:ital,wght@1,700&display=swap">
<style>
  :root {
    --brand-pink: #d6235d;
    --brand-pink-deep: #c01a52;
    --ink: #1b1b1b;
    --paper: #ffffff;
    --rule: #e58aa6;
    --tile-light: #f3e9ec;
    --tile-dark: #2c2c2e;
    --stage: #ecebe8;
  }
  * { box-sizing: border-box; margin: 0; padding: 0; }
  html, body {
    width: 1200px; height: 780px; overflow: hidden;
    background: var(--stage);
    font-family: "Nunito Sans", "Avenir", sans-serif;
  }
  .stage {
    position: relative; width: 1200px; height: 780px;
    display: flex; justify-content: center; align-items: center; gap: 120px;
  }
  .card {
    position: relative; width: 340px; height: 560px;
    border-radius: 22px; overflow: hidden;
    box-shadow: 0 10px 30px rgba(0,0,0,0.18);
  }

  /* Front */
  .card--front { background: var(--paper); color: var(--ink); }
  .card__texture {
    position: absolute; inset: 0;
    background:
      radial-gradient(ellipse at 20% 35%, var(--tile-light) 0%, transparent 45%),
      radial-gradient(ellipse at 85% 60%, var(--tile-light) 0%, transparent 40%),
      radial-gradient(ellipse at 30% 80%, var(--tile-light) 0%, transparent 40%);
    opacity: 0.8;
  }
  .brand {
    position: absolute; top: 62px; left: 0; right: 0;
    display: flex; align-items: center; justify-content: center; gap: 14px;
  }
  .brand__mark { width: 46px; height: 46px; background: var(--brand-pink); }
  .brand__name {
    font-weight: 800; font-size: 34px; letter-spacing: 2px; color: var(--ink);
    line-height: 1;
  }
  .contact {
    position: absolute; top: 170px; left: 30px; right: 30px;
    text-align: center;
  }
  .contact__name {
    font-weight: 800; font-size: 21px; letter-spacing: 1.5px;
    text-transform: uppercase; color: var(--brand-pink);
  }
  .contact__role { font-size: 16px; letter-spacing: 1px; margin-top: 2px; }
  .contact__rule { height: 1px; background: var(--rule); margin: 16px 10px 10px; }
  .contact__label {
    font-family: "Playfair Display", serif; font-style: italic; font-weight: 700;
    font-size: 13px; color: var(--brand-pink);
  }
  .contact__value { font-size: 17px; letter-spacing: 1px; margin-top: 2px; }
  .contact__address { font-size: 16px; letter-spacing: 0.8px; line-height: 1.5; margin-top: 4px; }
  .card__band {
    position: absolute; left: 0; right: 0; bottom: 0; height: 64px;
    background: var(--brand-pink);
    display: flex; align-items: center; justify-content: center;
    color: var(--paper); font-size: 17px; letter-spacing: 3px;
  }

  /* Back */
  .card--back { background: var(--ink); }
  .card__texture--dark {
    position: absolute; inset: 0;
    background:
      radial-gradient(ellipse at 25% 20%, var(--tile-dark) 0%, transparent 40%),
      radial-gradient(ellipse at 80% 35%, var(--tile-dark) 0%, transparent 35%),
      radial-gradient(ellipse at 40% 85%, var(--tile-dark) 0%, transparent 40%);
  }
  .brand--back { top: 50%; transform: translateY(-50%); }
  .brand--back .brand__name { color: var(--paper); }
</style>
</head>
<body>
  <main class="stage">
    <section class="card card--front" aria-label="Business card front">
      <div class="card__texture" role="img" aria-label="Faint tiled square background pattern"></div>
      <div class="brand">
        <span class="brand__mark"></span>
        <span class="brand__name">KVT LEGAL</span>
      </div>
      <div class="contact">
        <p class="contact__name">Boris Telemark</p>
        <p class="contact__role">Partner</p>
        <div class="contact__rule"></div>
        <p class="contact__label">Cell:</p>
        <p class="contact__value">0438 715 642</p>
        <div class="contact__rule"></div>
        <p class="contact__label">Email:</p>
        <p class="contact__value">boris@kvtlaw.co</p>
        <div class="contact__rule"></div>
        <p class="contact__address">Level 3, 118 Wexbury Street<br>Sydney NSW 2000</p>
      </div>
      <div class="card__band">www.kvtlaw.co</div>
    </section>

    <section class="card card--back" aria-label="Business card back">
      <div class="card__texture--dark" role="img" aria-label="Subtle dark tiled square background pattern"></div>
      <div class="brand brand--back">
        <span class="brand__mark"></span>
        <span class="brand__name">KVT LEGAL</span>
      </div>
    </section>
  </main>
</body>
</html>
```